my catalog design project for KTR tradeshow

We need a catalog design for our ranch equipment manufacturing company. The final design should communicate low cost alternative without compromising quality.
We need all the main product lines show cased in catalog including gates, panels, feeders, cattle squeezes, horse stalls, dog kennels, tractor attachments
The layout, design and colors can reflect the design of the website:

We just need a basic product catalog that uses a similar layout, design, and colors as our website: hollowcrestfabricating.com

Catalog should be approximately 6-10 pages long 8.5"x11" first page cover, next inside page company info, then product pages with item picture and description as in the website. For sample submissions, i'd like to see cover page, inside page and a product page.

FOR THE INITIAL ENTRIES, I'm expecting to see
- the cover page,
- inside company info page
- and one product page.

Target Market(s)

Chain Store buyers

Industry/Entity Type

Agriculture

Requirements
Must have
• All the product info details of main products

```html
<!DOCTYPE html>
<html lang="en">
<head>
<meta charset="utf-8">
<title>Hollowcrest Catalog – About Spread</title>
<link rel="stylesheet" href="https://fonts.googleapis.com/css2?family=Open+Sans:wght@400;600;700&display=swap">
<style>
  :root {
    --backdrop: #b5b5b5;
    --paper: #ffffff;
    --paper-shade: #eeeeee;
    --brand-red: #c8161f;
    --brand-red-dark: #8f0d14;
    --tab-black: #1a1a1a;
    --ink: #2a2a2a;
    --ink-soft: #5a5a5a;
    --bullet: #c9cdd0;
    --photo-sky: #c9d3dc;
    --photo-ground: #6f7a4c;
    --photo-steel: #4a8fd0;
  }
  * { box-sizing: border-box; margin: 0; padding: 0; }
  html, body { width: 1200px; height: 900px; overflow: hidden; }
  body {
    background: var(--backdrop);
    font-family: "Open Sans", Arial, sans-serif;
    position: relative;
  }
  .spread {
    position: absolute;
    left: 50px; top: 175px;
    width: 1100px; height: 550px;
    display: flex;
    box-shadow: 0 14px 30px rgba(0,0,0,.25);
  }
  .page {
    position: relative;
    width: 550px; height: 550px;
    background: var(--paper);
    overflow: hidden;
  }
  .page--left { background: linear-gradient(90deg, var(--paper) 85%, var(--paper-shade) 100%); }
  .page--right { background: linear-gradient(90deg, var(--paper-shade) 0%, var(--paper) 12%); }

  .section-panel { position: absolute; left: 0; top: 0; }
  .section-title {
    position: absolute; left: 150px; top: 152px;
    color: #fff; font-weight: 700; font-size: 22px;
  }
  .product-index { list-style: none; }
  .product-index li {
    position: absolute;
    color: #fff; font-size: 13px; font-weight: 600;
    text-align: right; width: 180px;
    transform: translateX(-100%);
    white-space: nowrap;
  }

  .wordmark {
    position: absolute; top: 70px; right: 40px;
    display: flex; align-items: center; gap: 8px;
    color: var(--brand-red);
    font-weight: 700; font-size: 26px; letter-spacing: 1px;
  }
  .wordmark__dot {
    width: 16px; height: 16px; border-radius: 50%;
    background: var(--brand-red);
  }

  .intro {
    position: absolute; right: 40px; top: 180px;
    width: 270px; text-align: right; color: var(--ink);
  }
  .intro h2 { font-size: 15px; font-weight: 700; margin-bottom: 10px; }
  .intro p { font-size: 11.5px; line-height: 1.6; color: var(--ink-soft); margin-bottom: 22px; }

  .photo { position: absolute; left: 0; top: 0; }
</style>
</head>
<body>
  <main class="spread">
    <section class="page page--left">
      <svg class="section-panel" width="550" height="550" viewBox="0 0 550 550" aria-hidden="true">
        <defs>
          <linearGradient id="redFill" x1="0" y1="0" x2="1" y2="1">
            <stop offset="0" stop-color="var(--brand-red-dark)"/>
            <stop offset="1" stop-color="var(--brand-red)"/>
          </linearGradient>
        </defs>
        <polygon points="0,180 240,180 150,550 0,550" fill="url(#redFill)"/>
        <polygon points="0,145 270,145 262,180 0,180" fill="var(--tab-black)"/>
        <g fill="var(--bullet)" stroke="#fff" stroke-width="1.5">
          <circle cx="232" cy="216" r="6"/>
          <circle cx="222" cy="254" r="6"/>
          <circle cx="212" cy="292" r="6"/>
          <circle cx="202" cy="330" r="6"/>
          <circle cx="192" cy="368" r="6"/>
          <circle cx="182" cy="406" r="6"/>
          <circle cx="172" cy="444" r="6"/>
          <circle cx="162" cy="482" r="6"/>
        </g>
      </svg>
      <div class="section-title">About</div>
      <ul class="product-index">
        <li style="left:220px;top:207px">Gates</li>
        <li style="left:210px;top:245px">Panels</li>
        <li style="left:200px;top:283px">Frame Gates</li>
        <li style="left:190px;top:321px">Feeders</li>
        <li style="left:180px;top:359px">Continuous Fence</li>
        <li style="left:170px;top:397px">Wall Feed Panels</li>
        <li style="left:160px;top:435px">Cattle Guard</li>
        <li style="left:150px;top:473px">Cattle Squeezes</li>
      </ul>

      <div class="wordmark"><span class="wordmark__dot"></span>HOLLOWCREST</div>

      <article class="intro">
        <h2>Here's what you can expect from Hollowcrest</h2>
        <p>A family-owned shop serving ranchers for over twenty years, we build durable livestock equipment at fair prices. Every gate, panel and feeder is welded in-house and checked by hand before it leaves our yard.</p>
        <h2>Where do we go from here?</h2>
        <p>Browse the pages ahead to find the product lines that fit your operation. Each listing shows sizes, gauges and options, so you can order with confidence. Call our team anytime for help.</p>
      </article>
    </section>

    <section class="page page--right">
      <svg class="photo" width="550" height="550" viewBox="0 0 550 550" role="img" aria-label="Photograph of blue portable fence panels and wire fencing on a gravel yard">
        <defs>
          <linearGradient id="photoTone" x1="0" y1="0" x2="0" y2="1">
            <stop offset="0" stop-color="var(--photo-sky)"/>
            <stop offset=".5" stop-color="#9aa59a"/>
            <stop offset=".75" stop-color="var(--photo-ground)"/>
            <stop offset="1" stop-color="#8b8b84"/>
          </linearGradient>
        </defs>
        <polygon points="0,0 340,0 230,550 0,550" fill="url(#photoTone)"/>
      </svg>
      <div class="wordmark"><span class="wordmark__dot"></span>HOLLOWCREST</div>
    </section>
  </main>
</body>
</html>
```